Tall Cedar Builders Business Card

I'm looking for a business card design for a start-up Handyman/Construction Company. The organization will double as a ministry to the homeless, hoping to create job opportunity and training to the homeless, providing a pathway back to being "homed". I'm looking for a simple to "seeming" simple design. Open to all thoughts.

Industry/Entity Type

Ministry

Requirements
Must have
• Logo (Attached), Name, Phone, Email and Address. Note - "*Registered and Insured".

```html
<!DOCTYPE html>
<html lang="en">
<head>
<meta charset="utf-8">
<title>Tall Cedar Builders Business Card</title>
<link rel="stylesheet" href="https://fonts.googleapis.com/css2?family=Open+Sans:wght@400;600;700;800&display=swap">
<style>
  :root {
    --page-bg: #d9dbde;
    --card-frost: #f3f4f6;
    --ink: #2b2740;
    --purple-deep: #5c2483;
    --purple-mid: #8a4bb0;
    --purple-soft: #e6d7ee;
    --swoosh-grey: #9a9ca3;
    --light-text: #ffffff;
  }
  * { margin: 0; padding: 0; box-sizing: border-box; }
  html, body {
    width: 1200px;
    height: 952px;
    overflow: hidden;
    background: var(--page-bg);
    font-family: "Open Sans", Arial, sans-serif;
  }
  .business-card {
    position: absolute;
    left: 100px;
    top: 186px;
    width: 1000px;
    height: 580px;
    border-radius: 14px;
    overflow: hidden;
    background: var(--card-frost);
    box-shadow: 0 18px 40px rgba(40, 30, 60, 0.18);
  }
  .card-waves {
    position: absolute;
    inset: 0;
    width: 1000px;
    height: 580px;
  }
  .brand {
    position: absolute;
    left: 70px;
    top: 62px;
  }
  .brand-name {
    display: flex;
    align-items: center;
    gap: 14px;
    font-weight: 800;
    font-size: 46px;
    line-height: 1;
    color: var(--ink);
    letter-spacing: 0.5px;
  }
  .brand-mark {
    width: 22px;
    height: 22px;
    background: var(--purple-deep);
  }
  .brand-tagline {
    margin-top: 14px;
    margin-left: 36px;
    font-weight: 700;
    font-size: 17px;
    letter-spacing: 5px;
    color: var(--ink);
    text-transform: uppercase;
  }
  .person {
    position: absolute;
    left: 78px;
    top: 292px;
    width: 600px;
    padding-bottom: 6px;
    border-bottom: 2px solid var(--ink);
    font-weight: 700;
    font-size: 22px;
    line-height: 30px;
    white-space: nowrap;
    color: var(--ink);
    text-transform: uppercase;
  }
  .person-divider { margin: 0 10px; font-weight: 400; }
  .person-title { font-weight: 600; }
  .contact {
    position: absolute;
    display: flex;
    flex-direction: column;
    gap: 10px;
    font-size: 19px;
    line-height: 26px;
    color: var(--light-text);
  }
  .contact-left { left: 78px; top: 348px; }
  .contact-right { left: 560px; top: 348px; }
  .contact-address { color: var(--ink); }
  .contact-row {
    display: flex;
    align-items: center;
    gap: 14px;
    white-space: nowrap;
  }
  .contact-icon { width: 18px; height: 18px; flex: none; }
</style>
</head>
<body>
  <div class="business-card">
    <svg class="card-waves" viewBox="0 0 1000 580" aria-hidden="true">
      <defs>
        <linearGradient id="bandFill" x1="0" y1="1" x2="1" y2="0">
          <stop offset="0" stop-color="var(--purple-deep)"/>
          <stop offset="0.45" stop-color="var(--purple-mid)"/>
          <stop offset="1" stop-color="var(--purple-soft)"/>
        </linearGradient>
      </defs>
      <path d="M0,250 C180,300 320,290 470,230 C620,170 800,120 1000,130 L1000,580 L0,580 Z" fill="url(#bandFill)"/>
      <path d="M0,250 C180,300 320,290 470,230 C620,170 800,120 1000,130" fill="none" stroke="var(--card-frost)" stroke-width="10" opacity="0.7"/>
      <path d="M40,262 C220,300 340,280 480,218 C630,152 790,112 1000,112" fill="none" stroke="var(--purple-deep)" stroke-width="4"/>
      <path d="M360,250 C500,200 640,130 820,100 C890,90 950,90 1000,92" fill="none" stroke="var(--swoosh-grey)" stroke-width="3"/>
      <path d="M420,232 C560,170 700,112 1000,100" fill="none" stroke="var(--swoosh-grey)" stroke-width="1.5" opacity="0.7"/>
    </svg>

    <div class="brand">
      <div class="brand-name"><span class="brand-mark"></span>Tall Cedar Builders</div>
      <div class="brand-tagline">Registered and Insured</div>
    </div>

    <div class="person">
      <span class="person-name">Mara Ellison</span><span class="person-divider">|</span><span class="person-title">Chief Executive Officer</span>
    </div>

    <div class="contact contact-left">
      <div class="contact-row contact-address">
        <svg class="contact-icon" viewBox="0 0 24 24"><path d="M12 2a7 7 0 0 0-7 7c0 5 7 13 7 13s7-8 7-13a7 7 0 0 0-7-7zm0 9.5A2.5 2.5 0 1 1 12 6.5a2.5 2.5 0 0 1 0 5z" fill="currentColor"/></svg>
        4120 Harbor Lane, Albany, NY 12207
      </div>
      <div class="contact-row">
        <svg class="contact-icon" viewBox="0 0 24 24"><path d="M6.6 10.8a15.5 15.5 0 0 0 6.6 6.6l2.2-2.2a1 1 0 0 1 1-.25 11.4 11.4 0 0 0 3.6.57 1 1 0 0 1 1 1V20a1 1 0 0 1-1 1A17 17 0 0 1 3 4a1 1 0 0 1 1-1h3.5a1 1 0 0 1 1 1c0 1.25.2 2.45.57 3.6a1 1 0 0 1-.25 1z" fill="currentColor"/></svg>
        555-310-2188
      </div>
      <div class="contact-row">
        <svg class="contact-icon" viewBox="0 0 24 24"><rect x="6" y="2" width="12" height="20" rx="2" fill="none" stroke="currentColor" stroke-width="2"/><circle cx="12" cy="18" r="1.3" fill="currentColor"/></svg>
        555-806-4471
      </div>
    </div>

    <div class="contact contact-right">
      <div class="contact-row">
        <svg class="contact-icon" viewBox="0 0 24 24"><rect x="2" y="5" width="20" height="14" rx="1.5" fill="none" stroke="currentColor" stroke-width="2"/><path d="M3 6l9 7 9-7" fill="none" stroke="currentColor" stroke-width="2"/></svg>
        info@tallcedarbuilders.com
      </div>
      <div class="contact-row">
        <svg class="contact-icon" viewBox="0 0 24 24"><circle cx="12" cy="12" r="9" fill="none" stroke="currentColor" stroke-width="2"/><path d="M3 12h18M12 3c3 3 3 15 0 18M12 3c-3 3-3 15 0 18" fill="none" stroke="currentColor" stroke-width="1.6"/></svg>
        www.tallcedarbuilders.com
      </div>
    </div>
  </div>
</body>
</html>
```